Business Card Design

This is a coaching and training company. We deliver personal development workshops, training and one to one coaching. We would like the current logo to be used.

Target Market(s)

For coaches, small business owners and people aged around 40-60 who are seeking direction in their life

Industry/Entity Type

Training

Contact Information for Business Card

Marion Tuckett
Speaker-Trainer-Coach
There is no going back ...
0461 738196
18 Harrow Lane Pembry
mtuckett47@quillbox.net

Font styles to use
Sans Serif

Requirements
Should not have
• No old style fonts

```html
<!DOCTYPE html>
<html lang="en">
<head>
<meta charset="utf-8">
<title>Tessaly Coaching and Training Solutions – Business Card</title>
<link rel="stylesheet" href="https://fonts.googleapis.com/css2?family=Marcellus+SC&family=Josefin+Sans:ital,wght@0,400;0,600;1,400&display=swap">
<style>
  :root{
    --sky:#33acdc;
    --sky-light:#55bde6;
    --teal:#1a6f8f;
    --brand:#2a8fc4;
    --ink-grey:#5d6266;
    --mark-grey:#e3e6e9;
    --paper:#ffffff;
    --backdrop:#eef0f2;
  }
  *{box-sizing:border-box;margin:0;padding:0}
  html,body{width:1200px;height:1000px;overflow:hidden;background:var(--backdrop)}
  body{position:relative;font-family:"Josefin Sans",sans-serif}

  .card{position:absolute;left:220px;width:760px;height:434px;background:var(--paper);overflow:hidden;box-shadow:0 6px 22px rgba(0,0,0,.14)}
  .card--front{top:40px}
  .card--back{top:526px}

  /* front */
  .front__panel{position:absolute;left:426px;top:0;right:0;bottom:0;background:linear-gradient(180deg,var(--sky) 0%,var(--sky) 45%,var(--sky-light) 100%)}
  .name-band{position:absolute;left:400px;top:110px;width:360px;height:84px;background:var(--teal);color:var(--paper);padding:14px 0 0 46px}
  .name-band__name{font-family:"Marcellus SC",serif;font-size:38px;letter-spacing:1.5px;line-height:1}
  .name-band__role{font-style:italic;font-size:14px;letter-spacing:1px;text-transform:uppercase;margin:8px 0 0 70px}

  .contact-list{position:absolute;left:466px;top:246px;list-style:none;color:var(--paper)}
  .contact-list__item{display:flex;align-items:center;height:44px;font-size:16px;letter-spacing:1.2px}
  .contact-list__item--phone{font-size:21px;letter-spacing:2px}
  .contact-list__item--small{text-transform:uppercase;font-size:15px}
  .contact-list__icon{width:30px;height:30px;margin-right:12px;flex:none}

  .brand{position:absolute;left:60px;top:78px;width:300px;text-align:center}
  .brand__square{width:150px;height:150px;margin:0 auto 26px;background:var(--mark-grey)}
  .brand__name{font-family:"Marcellus SC",serif;font-size:50px;color:var(--brand);letter-spacing:2px;line-height:1}
  .brand__tagline{font-family:"Marcellus SC",serif;font-size:16px;color:var(--ink-grey);margin-top:10px;letter-spacing:.3px}

  /* back */
  .back__band-top{position:absolute;left:0;top:0;width:436px;height:110px;background:var(--sky)}
  .back__band-side{position:absolute;left:0;top:110px;width:330px;height:220px;background:var(--sky)}
  .back__brand{position:absolute;left:440px;top:140px;width:240px;text-align:center}
  .back__brand .brand__square{width:100px;height:100px;margin-bottom:16px}
  .back__brand .brand__name{font-size:32px}
  .back__brand .brand__tagline{font-size:11px;margin-top:6px}
  .back__motto{position:absolute;left:40px;top:362px;font-size:30px;letter-spacing:2px;color:var(--brand);text-transform:uppercase}
</style>
</head>
<body>

<section class="card card--front" aria-label="Business card front">
  <div class="brand">
    <div class="brand__square"></div>
    <div class="brand__name">TESSALY</div>
    <div class="brand__tagline">Coaching and Training Solutions</div>
  </div>

  <div class="front__panel"></div>

  <div class="name-band">
    <div class="name-band__name">Marion Tuckett</div>
    <div class="name-band__role">Speaker-Trainer-Coach</div>
  </div>

  <ul class="contact-list">
    <li class="contact-list__item contact-list__item--phone">
      <svg class="contact-list__icon" viewBox="0 0 30 30" aria-hidden="true"><rect x="9" y="2" width="12" height="26" rx="3" fill="#fff"/><rect x="11" y="6" width="8" height="13" fill="#33acdc"/><circle cx="15" cy="23.5" r="1.6" fill="#33acdc"/></svg>
      0461 738196
    </li>
    <li class="contact-list__item contact-list__item--small">
      <svg class="contact-list__icon" viewBox="0 0 30 30" aria-hidden="true"><g fill="none" stroke="#fff" stroke-width="1.8"><circle cx="15" cy="15" r="12"/><ellipse cx="15" cy="15" rx="5.5" ry="12"/><line x1="3" y1="15" x2="27" y2="15"/><path d="M5 9h20M5 21h20"/></g></svg>
      www.tessalycts.com
    </li>
    <li class="contact-list__item contact-list__item--small">
      <svg class="contact-list__icon" viewBox="0 0 30 30" aria-hidden="true"><rect x="2" y="7" width="26" height="17" fill="#fff"/><path d="M2 7l13 10 13-10" fill="none" stroke="#33acdc" stroke-width="1.8"/></svg>
      marion@tessalycts.com
    </li>
  </ul>
</section>

<section class="card card--back" aria-label="Business card back">
  <div class="back__band-top"></div>
  <div class="back__band-side"></div>
  <div class="back__brand">
    <div class="brand__square"></div>
    <div class="brand__name">TESSALY</div>
    <div class="brand__tagline">Coaching and Training Solutions</div>
  </div>
  <div class="back__motto">There is no going back.....</div>
</section>

</body>
</html>
```